Professional Business Card for Commercial Cleaning Company

We need a business card that represents our commercial janitorial cleaning company and represent several brands for our company so we do not want to highlight the logo too much. We want something that says we are professional.
Notes:No website or address as we have many locations and many websites and companies under our corporate name of "Brightvale Holdings, LLC" . Every time we hand a customer a business card they have contacted us via another brand we own but we don't want to have 21 business cards so we want to not focus on Brightvale Holdings, LLC too much since people will automatically ask "What is Brightvale Holdings, LLC" Example: Noodle Barn and Wrap Lantern restaurants are owned by "Zest! Brands" is the corporation name. Same principle here. Except we do not advertise at this time that all of our brands are connected. Hope this helps.
Target Market(s)
Commercial Cleaning
Industry/Entity Type
Janitorial Service
Contact Information for Business Card
Milo Jarvis
Business Development
555-382-9047
sales@brightvaleholdingsllc.example
Requirements
Must have
- Logo with contact information, need to be able to easily edit contact info for others in my office.
Nice to have
- Professional Image. Like to see a colorful bold look and a more standard business card look.
Should not have
- Any type of cleaning icons, tools, people or water.

```html
<!DOCTYPE html>
<html lang="en">
<head>
<meta charset="utf-8">
<title>Brightvale Holdings, LLC – Business Card</title>
<link rel="stylesheet" href="https://fonts.googleapis.com/css2?family=Lato:wght@400;700&display=swap">
<style>
  :root {
    --navy: #213f7a;
    --green: #6aa343;
    --white: #ffffff;
    --page: #e6e7ea;
    --shadow: rgba(20, 24, 40, 0.18);
  }
  * { margin: 0; padding: 0; box-sizing: border-box; }
  html, body {
    width: 1200px;
    height: 800px;
    overflow: hidden;
    background: var(--page);
    font-family: "Lato", Arial, sans-serif;
  }
  .canvas {
    position: relative;
    width: 1200px;
    height: 800px;
  }
  .card {
    position: absolute;
    left: 320px;
    width: 560px;
    height: 320px;
    background: var(--white);
    box-shadow: 0 10px 30px var(--shadow);
    overflow: hidden;
  }
  .card--front { top: 50px; }
  .card--back { top: 420px; }

  .wordmark {
    position: absolute;
    color: var(--navy);
    font-weight: 700;
    white-space: nowrap;
    letter-spacing: 0.2px;
    line-height: 1.2;
  }
  .card--front .wordmark {
    left: 0; right: 0; top: 136px;
    text-align: center;
    font-size: 40px;
  }
  .card--back .wordmark {
    left: 44px; top: 46px;
    font-size: 28px;
  }

  .card-bands {
    position: absolute;
    inset: 0;
    width: 560px;
    height: 320px;
  }
  .band--navy { fill: var(--navy); }
  .band--green { fill: var(--green); }

  .contact {
    position: absolute;
    color: var(--white);
  }
  .contact-person { left: 30px; top: 248px; }
  .contact-name { font-size: 17px; font-weight: 700; line-height: 1.1; }
  .contact-title { font-size: 12px; font-weight: 400; margin-top: 2px; }
  .contact-line {
    display: flex;
    align-items: center;
    gap: 7px;
    font-size: 12.5px;
  }
  .contact-phone { left: 30px; top: 292px; }
  .contact-email { right: 24px; top: 198px; }
  .contact-icon { width: 13px; height: 13px; flex: none; }
</style>
</head>
<body>
<main class="canvas">
  <section class="card card--front" aria-label="Business card front">
    <div class="wordmark">Brightvale Holdings, LLC</div>
  </section>

  <section class="card card--back" aria-label="Business card back">
    <svg class="card-bands" viewBox="0 0 560 320" aria-hidden="true">
      <path class="band--green" d="M0 206 C230 180 410 120 466 36 C424 126 240 202 0 228 Z"/>
      <path class="band--navy" d="M0 238 C250 200 450 140 492 0 L560 0 L560 320 L0 320 Z"/>
    </svg>

    <div class="wordmark">Brightvale Holdings, LLC</div>

    <div class="contact contact-person">
      <div class="contact-name">Milo Jarvis</div>
      <div class="contact-title">Business Development</div>
    </div>

    <div class="contact contact-line contact-phone">
      <svg class="contact-icon" viewBox="0 0 14 14" aria-hidden="true">
        <rect x="3.5" y="1" width="7" height="12" rx="1.2" fill="none" stroke="#fff" stroke-width="1.4"/>
      </svg>
      <span>555-382-9047</span>
    </div>

    <div class="contact contact-line contact-email">
      <svg class="contact-icon" viewBox="0 0 14 14" aria-hidden="true">
        <rect x="1" y="3" width="12" height="8.5" fill="#fff"/>
        <path d="M1 3 L7 8 L13 3" fill="none" stroke="#213f7a" stroke-width="1.2"/>
      </svg>
      <span>sales@brightvaleholdingsllc.example</span>
    </div>
  </section>
</main>
</body>
</html>
```